Commercial HVAC and Refrigeration Business cards

Frost-Haven Company is looking for flashy new business cards! We design, install, service and maintain commercial refrigeration, air conditioning, heating and refrigeration equipment. Our colors are blue and white. I'm open to single and double sided designs. Each employee will have their own business card. I've attached a copy of our current logo.

Our website, office and cell phone (cell phone is optional), email address should be clearly legible. "24 Hour Service" and the services we offer are; Sales, Service, Design, Installation, Maintenance. Refrigeration, Heating, Air Conditioning, Ice Machines. Does not have to be in any order.

Target Market(s)

Commercial; Restaurants, hotels, bars, breweries etc.

Industry/Entity Type

Hvac

Contact Information for Business Card

Name; Job Title, Phone Number, Email Address. www.frost-haven-example.com 24 Hour Service. We provide - Sales, Design, Installation, Service, Maintenance. We service - Refrigeration, Heating, Air Conditioning, Ice Machines

Font styles to use
Other font styles liked:
• Be creative

Colors
0255a3
ffffff

Requirements
Must have
• Professional appearance and appeal to commercial clients in the food-service and hospitality industry. Must be clearly legible and easy to understand.
Nice to have
• We want to sell maintenance agreements, perhaps we can use the back of the card to tie into a webpage about our maintenance agreements.
Should not have
• Cartoons or unprofessional. Nothing too edgy.

```html
<!DOCTYPE html>
<html lang="en">
<head>
<meta charset="utf-8">
<title>Frost-Haven Company – Business Cards</title>
<link rel="stylesheet" href="https://fonts.googleapis.com/css2?family=EB+Garamond:wght@400;500&family=Open+Sans:wght@700&display=swap">
<style>
  :root {
    --brand-blue: #0255a3;
    --deep-blue: #1c4f96;
    --paper: #ffffff;
    --ink: #1d1d1f;
    --ink-soft: #3a3a3f;
    --badge-blue: #a9bed6;
    --badge-fill: #e3eaf2;
    --backdrop: #e9e7e3;
  }
  * { box-sizing: border-box; margin: 0; padding: 0; }
  html, body { width: 1200px; height: 892px; overflow: hidden; }
  body {
    background: var(--backdrop);
    font-family: "EB Garamond", Georgia, serif;
    color: var(--ink);
    display: flex;
    flex-direction: column;
    align-items: center;
    justify-content: center;
    gap: 40px;
  }
  .card {
    position: relative;
    width: 640px;
    height: 366px;
    background: var(--paper);
    box-shadow: 0 2px 10px rgba(0,0,0,.12);
    overflow: hidden;
  }

  /* Front */
  .card-front .identity {
    position: absolute;
    left: 150px; top: 46px;
  }
  .identity .person-name { font-size: 27px; font-weight: 400; letter-spacing: .5px; }
  .identity .person-title { font-size: 18px; color: var(--ink-soft); margin-top: 2px; }
  .card-front .rule {
    position: absolute;
    left: 56px; top: 132px;
    width: 250px; height: 2px;
    background: var(--brand-blue);
  }
  .contact-list {
    position: absolute;
    left: 56px; top: 154px;
    width: 250px;
    list-style: none;
    font-size: 15px;
    color: var(--ink-soft);
    line-height: 22px;
  }
  .contact-list li { display: flex; align-items: flex-start; gap: 10px; }
  .contact-list svg { flex: none; margin-top: 2px; }
  .card-front .brand-name {
    position: absolute;
    right: 34px; top: 250px;
    font-size: 30px;
    font-weight: 500;
    color: var(--brand-blue);
    display: flex; align-items: center; gap: 10px;
    white-space: nowrap;
  }
  .brand-mark { width: 14px; height: 14px; background: var(--brand-blue); flex: none; }

  /* Back */
  .card-back .edge-band {
    position: absolute; left: 0; top: 0; bottom: 0;
    width: 14px; background: var(--deep-blue);
  }
  .emergency-badge {
    position: absolute; left: 46px; top: 34px;
    width: 150px; height: 150px;
    border-radius: 50%;
    border: 6px solid var(--badge-fill);
    background: var(--badge-fill);
    box-shadow: inset 0 0 0 3px var(--badge-blue);
    display: flex; align-items: center; justify-content: center;
    text-align: center;
    font-family: "Open Sans", Arial, sans-serif;
    font-weight: 700;
    font-size: 17px;
    line-height: 20px;
    color: var(--badge-blue);
    transform: rotate(-8deg);
  }
  .card-back .brand-name {
    position: absolute; left: 230px; right: 20px; top: 96px;
    text-align: center;
    font-size: 32px; font-weight: 500;
    color: var(--brand-blue);
    white-space: nowrap;
  }
  .services {
    position: absolute; left: 200px; right: 60px; top: 160px;
  }
  .services-heads {
    display: grid; grid-template-columns: 1fr 30px 1fr;
    font-size: 21px;
    padding-bottom: 6px;
    border-bottom: 2px solid var(--brand-blue);
  }
  .services-heads span:first-child { text-align: right; }
  .services-cols {
    display: grid; grid-template-columns: 1fr 30px 1fr;
    margin-top: 8px;
    font-size: 22px; line-height: 26px;
  }
  .services-cols ul { list-style: none; }
  .services-cols .left { text-align: right; white-space: nowrap; }
  .services-cols .dots { display: flex; flex-direction: column; align-items: center; }
  .services-cols .dots i {
    display: block; width: 9px; height: 9px; border-radius: 50%;
    background: var(--deep-blue); margin: 9px 0 8px;
  }
</style>
</head>
<body>

  <section class="card card-front" aria-label="Business card front">
    <div class="identity">
      <h1 class="person-name">Daniel Marlowe</h1>
      <p class="person-title">President</p>
    </div>
    <div class="rule"></div>
    <ul class="contact-list">
      <li>
        <svg width="16" height="16" viewBox="0 0 18 18" aria-hidden="true"><rect width="18" height="18" rx="4" fill="#0255a3"/><path d="M5 4.5c.6-.4 1.4-.3 1.8.3l.8 1.3c.3.5.2 1.1-.2 1.4l-.5.4c.5 1.1 1.3 1.9 2.4 2.4l.4-.5c.4-.4 1-.5 1.4-.2l1.3.8c.6.4.7 1.2.3 1.8-.6.8-1.6 1.1-2.5.7-2.4-1-4.3-2.9-5.3-5.3-.4-.9-.1-1.9.7-2.5z" fill="#fff"/></svg>
        <span>(555) 014-2260</span>
      </li>
      <li>
        <svg width="16" height="16" viewBox="0 0 18 18" aria-hidden="true"><rect width="18" height="18" rx="4" fill="#0255a3"/><rect x="4" y="5.5" width="10" height="7" rx="1" fill="none" stroke="#fff" stroke-width="1.3"/><path d="M4.3 6l4.7 3.6L13.7 6" fill="none" stroke="#fff" stroke-width="1.3"/></svg>
        <span>info@frost-haven-example.com</span>
      </li>
      <li>
        <svg width="16" height="16" viewBox="0 0 18 18" aria-hidden="true"><rect width="18" height="18" rx="4" fill="#0255a3"/><circle cx="9" cy="9" r="4.8" fill="none" stroke="#fff" stroke-width="1.2"/><ellipse cx="9" cy="9" rx="2" ry="4.8" fill="none" stroke="#fff" stroke-width="1.1"/><path d="M4.2 9h9.6" stroke="#fff" stroke-width="1.1"/></svg>
        <span>www.frost-haven-example.com</span>
      </li>
      <li>
        <svg width="16" height="16" viewBox="0 0 18 18" aria-hidden="true"><rect width="18" height="18" rx="4" fill="#0255a3"/><path d="M9 14s-4-4.2-4-7a4 4 0 0 1 8 0c0 2.8-4 7-4 7z" fill="#fff"/><circle cx="9" cy="7" r="1.5" fill="#0255a3"/></svg>
        <span>1480 Harbor Point Drive,<br>Suite K, Millbrook,<br>MD 20000-0000</span>
      </li>
    </ul>
    <div class="brand-name"><span class="brand-mark" aria-hidden="true"></span>Frost-Haven Company</div>
  </section>

  <section class="card card-back" aria-label="Business card back">
    <div class="edge-band"></div>
    <div class="emergency-badge">24 HOUR<br>EMERGENCY<br>SERVICE</div>
    <div class="brand-name">Frost-Haven Company</div>
    <div class="services">
      <div class="services-heads"><span>We service</span><span></span><span>We provide</span></div>
      <div class="services-cols">
        <ul class="left">
          <li>Heating</li>
          <li>Ice Machines</li>
          <li>Refrigeration</li>
          <li>Air Conditioning</li>
        </ul>
        <div class="dots" aria-hidden="true"><i></i><i></i><i></i><i></i><i></i></div>
        <ul class="right">
          <li>Sales</li>
          <li>Design</li>
          <li>Service</li>
          <li>Installation</li>
          <li>Maintenance</li>
        </ul>
      </div>
    </div>
  </section>

</body>
</html>
```